Green blog

Hi there !
I want to redesign my french green blog here: http://www.verdanimo.info

I want the same presentation, but something much funny, professionnal and great !

I have a new logo to integrate it, i'll put it on the attachment.

Thank you so much for your work in advance !

Hello there !

The price is for only the design, not the wordpress integration !

Thanks

```html
<!DOCTYPE html>
<html lang="fr">
<head>
<meta charset="utf-8">
<title>Verdanimo, Penser nature</title>
<link rel="stylesheet" href="https://fonts.googleapis.com/css2?family=Arimo:wght@400;700&family=Tinos:ital,wght@0,400;0,700;1,400&family=Yanone+Kaffeesatz:wght@400;600;700&display=swap">
<style>
:root{
  --nav-top:#fbfbfb;--nav-bottom:#d9d9d9;--nav-text:#3a3a3a;
  --green-light:#a6d13b;--green:#6fae1c;--green-dark:#3e7a0d;
  --banner-green:#2f8a16;--banner-lime:#7cc21f;
  --page:#f2f2f2;--sidebar:#ebe8c6;--sidebar-edge:#d8d3a6;
  --post:#f0eed6;--post-edge:#cfc9a3;--ink:#2b2b1f;--muted:#6b6750;
  --link:#8a7a1a;--red:#c8231a;--badge:#f6a21a;--social:#5b77ad;--social-bar:#e6ebf4;
}
*{box-sizing:border-box;margin:0;padding:0}
html,body{width:1200px;height:882px;overflow:hidden}
body{position:relative;background:var(--page);font-family:"Arimo",Arial,sans-serif;color:var(--ink)}
.abs{position:absolute}
.topbar{left:0;top:0;width:1200px;height:60px;background:linear-gradient(var(--nav-top),var(--nav-bottom))}
.nav a{position:absolute;top:20px;font-size:15px;color:var(--nav-text);text-decoration:none}
.search-label{left:758px;top:21px;font-size:14px;color:var(--nav-text);white-space:nowrap}
.search-box{left:834px;top:16px;width:252px;height:24px;background:linear-gradient(#b8c0c7,#8f99a3);border:1px solid #7b858e;border-radius:3px}
.search-btn{left:1062px;top:19px;width:18px;height:18px;border-radius:50%;background:#e9eef2}
.masthead{left:0;top:60px;width:1200px;height:122px;background:linear-gradient(var(--green-light),var(--green) 60%,var(--green-dark))}
.brand-dot{left:134px;top:76px;width:64px;height:64px;border-radius:50%;background:#dfe9b5}
.brand-name{left:212px;top:84px;font-family:"Yanone Kaffeesatz",sans-serif;font-weight:600;font-size:48px;color:#fff4a8;letter-spacing:.5px}
.brand-tag{left:302px;top:138px;font-size:11px;letter-spacing:2px;color:#fff}
.tagline{left:636px;top:74px;font-family:"Yanone Kaffeesatz",sans-serif;font-weight:700;font-size:60px;color:#fff;white-space:nowrap}
.stone{left:128px;top:168px;width:298px;height:250px;background:radial-gradient(circle at 40% 40%,#b5b5b5,#7d7d7d)}
.banner{left:426px;top:180px;width:660px;height:228px;background:#fff}
.globe{left:14px;top:10px;width:196px;height:210px;border-radius:50%;background:radial-gradient(circle at 45% 55%,#d6ec3a,#3f9a18 70%,transparent 71%)}
.pitch{left:214px;top:10px;font-family:"Yanone Kaffeesatz",sans-serif;font-weight:700;color:var(--banner-green);line-height:1;text-align:center;width:440px}
.pitch .l1{font-size:54px}
.pitch .l2{font-size:40px;color:var(--banner-lime)}
.pitch .l3{font-size:34px;color:var(--banner-lime)}
.pitch .l4{font-size:54px}
.sidebar{left:128px;top:424px;width:298px;height:458px;background:var(--sidebar);box-shadow:inset 0 8px 10px -6px var(--sidebar-edge)}
.fanbox{left:34px;top:36px;width:236px;height:272px;background:#fff;border:1px solid #c9cfdc;font-size:11px;color:#333}
.fanbox-head{height:24px;background:var(--social-bar);border-bottom:1px solid #c9cfdc;padding:5px 8px;font-weight:700;color:#3b3b3b}
.fan-page{left:8px;top:36px;display:flex;gap:8px}
.thumb{width:36px;height:30px;background:#9bbd59}
.fan-page b{color:var(--social);font-size:12px}
.like{display:inline-block;margin-top:4px;padding:1px 6px;border:1px solid #b7c0d3;background:#eef1f7;font-size:10px;color:var(--social)}
.fan-count{left:8px;top:82px}
.faces{left:8px;top:100px;display:grid;grid-template-columns:repeat(4,44px);gap:6px 12px;text-align:center;font-size:9px}
.face{width:44px;height:38px;background:linear-gradient(#c9a98c,#8d6b53);margin-bottom:2px}
.fanbox-foot{left:0;bottom:0;width:100%;height:20px;border-top:1px solid #d5d9e3;padding:4px 8px;font-size:10px;color:#555}
.widget-title{left:0;top:336px;width:298px;text-align:center;font-family:"Tinos",serif;font-size:29px;color:#5a7a1a}
.col-head{top:374px;font-family:"Tinos",serif;font-size:15px;color:#333;border-bottom:1px solid #bdb78f;padding-bottom:5px;width:134px}
.col-text{top:404px;font-family:"Tinos",serif;font-size:15px;line-height:19px;color:#333;width:128px}
.red{color:var(--red)}
.content{left:466px;top:424px;width:620px;height:458px;background:var(--post);border:1px solid var(--post-edge);box-shadow:inset 0 8px 10px -6px var(--post-edge)}
.meta{left:12px;font-family:"Tinos",serif;font-size:13px;color:var(--muted)}
.meta a{color:var(--link)}
.post-title{left:12px;font-family:"Tinos",serif;color:var(--ink);width:596px;border-bottom:1px solid #9d987a;white-space:nowrap}
.t1{top:44px;font-size:31px;padding-bottom:4px}
.t2{top:322px;font-size:27px;font-weight:700;padding-bottom:6px;letter-spacing:-.2px}
.ant{left:24px;top:100px;width:156px;height:116px;background:linear-gradient(#d9d9ef,#7b7bb3);border:1px solid #888}
.excerpt{left:198px;top:106px;width:400px;font-family:"Tinos",serif;font-style:italic;font-size:12px;line-height:16px;color:#333}
.badge{left:502px;top:194px;padding:5px 8px;background:var(--badge);font-family:"Tinos",serif;font-weight:700;font-size:13px;color:#222}
.ad{left:12px;top:236px;width:596px;height:54px;border-top:1px solid #9d987a;border-bottom:1px solid #9d987a;padding:6px 32px;font-size:11px;color:#333}
.ad b{color:#1a3b8f;text-decoration:underline;font-size:12px}
.ad-by{right:72px;bottom:10px;font-size:10px;color:#444}
.excerpt2{left:12px;top:378px;width:596px;height:80px;border:1px solid #b3ae8d;padding:10px 10px;font-family:"Tinos",serif;font-style:italic;font-size:12px;line-height:16px;color:#333}
</style>
</head>
<body>
<header>
  <div class="abs topbar"></div>
  <nav class="nav">
    <a style="left:160px">A Propos</a>
    <a style="left:236px">Gestes simples</a>
    <a style="left:360px">Newsletter</a>
    <a style="left:448px">Produits écolo</a>
  </nav>
  <div class="abs search-label">Recherche</div>
  <div class="abs search-box"></div>
  <div class="abs search-btn"></div>

  <div class="abs masthead"></div>
  <div class="abs brand-dot"></div>
  <div class="abs brand-name">Verdanimo</div>
  <div class="abs brand-tag">PENSER NATURE</div>
  <div class="abs tagline">Verdanimo, Penser nature.</div>

  <div class="abs stone" role="img" aria-label="Photo de béton gravé du nom du blog"></div>
  <div class="abs banner">
    <div class="abs globe" role="img" aria-label="Illustration d'un globe vert avec une jeune pousse"></div>
    <div class="abs pitch">
      <div class="l1">Je choisis VERDANIMO</div>
      <div class="l2">pour ses qualités Schéma</div>
      <div class="l3">Lebelthermiques et phoniques</div>
      <div class="l4">incomparables</div>
    </div>
  </div>
</header>

<aside class="abs sidebar">
  <div class="abs fanbox">
    <div class="fanbox-head">Find us on Amigonet</div>
    <div class="abs fan-page">
      <div class="thumb" role="img" aria-label="Vignette du blog"></div>
      <div><b>Verdanimo, blog écologie</b><br><span class="like">Like</span></div>
    </div>
    <div class="abs fan-count">Verdanimo, blog écologie has 225 fans</div>
    <div class="abs faces">
      <div><div class="face" role="img" aria-label="Photo de fan"></div>Odile</div>
      <div><div class="face" role="img" aria-label="Photo de fan"></div>Karim</div>
      <div><div class="face" role="img" aria-label="Photo de fan"></div>Louis</div>
      <div><div class="face" role="img" aria-label="Photo de fan"></div>Maëlle</div>
      <div><div class="face" role="img" aria-label="Photo de fan"></div>Josette</div>
      <div><div class="face" role="img" aria-label="Photo de fan"></div>Sylvie</div>
      <div><div class="face" role="img" aria-label="Photo de fan"></div>nabil</div>
      <div><div class="face" role="img" aria-label="Photo de fan"></div>Paul</div>
    </div>
    <div class="abs fanbox-foot">Amigonet social plugin</div>
  </div>
  <h3 class="abs widget-title">Ecologie et Bio</h3>
  <div class="abs col-head" style="left:14px">Articles récents</div>
  <div class="abs col-head" style="left:154px">Energie solaire</div>
  <div class="abs col-text" style="left:14px">→ <span class="red">La crise ne doit pas faire oublier l'écologie</span></div>
  <div class="abs col-text" style="left:166px">Retrouvez toutes nos informations <span class="red">sur l'énergie</span></div>
</aside>

<main class="abs content">
  <div class="abs meta" style="top:16px">February 2, 2009 Posted bt administartor in : <a>Technology</a>.</div>
  <h2 class="abs post-title t1">Astuce 7: Faire fuire les fourmis</h2>
  <div class="abs ant" role="img" aria-label="Illustration d'une fourmi"></div>
  <p class="abs excerpt">"Lorem ipsum dolor sit amet, consectetur adipisicing elit, sed do eiusmod tempor incididunt ut labore et dolore magna aliqua. Ut enim ad minim veniam, quis nostrud exercitation ullamco laboris nisi ut aliquip ex ea consequat. Duis aute irure dolor in reprehenderit in voluptate velit esse dolore eu fugiat nulla pariatur. Excepteur sint occaecat cupidatat non sunt in culpa qui"</p>
  <div class="abs badge">2 Commentaire</div>
  <div class="abs ad">
    <b>Multi Screen Check</b><br>See how your website works &amp; looks in all browsers/OSs. Free trial!<br>MultiScreenCheck.com
    <div class="abs ad-by">Ads by Adnova</div>
  </div>
  <div class="abs meta" style="top:300px">February 2, 2009 Posted bt administartor in : <a>Entertainment</a>.</div>
  <h2 class="abs post-title t2">La crise ne doit pas faire oublier l'écologie</h2>
  <p class="abs excerpt2">"Lorem ipsum dolor sit amet, consectetur adipisicing elit, sed do eiusmod tempor incididunt ut labore et dolore magna aliqua. Ut enim ad minim veniam, quis nostrud exercitation ullamco laboris nisi ut aliquip ex ea consequat. Duis aute irure dolor in reprehenderit in voluptate velit esse dolore eu fugiat nulla pariatur.</p>
</main>
</body>
</html>
```